Alumni Ballot Postcard

We need a quick postcard to mail out to our alumni telling them that they are invited to vote on a new ballot of alumni officers. I purchased a 4 color picture I want to use for the front of the postcard from pixbarn but I can't get it to upload. Someone can email me at Marta.venn@sgfcollege-example.edu and I will email them the image. The final design needs to be clean and easy to read.

Offering doctoral, master’s, baccalaureate, and associate degrees, Saint Gideon of the Fields College is a four-year, independent Catholic institution, providing a strong foundation in the liberal arts and continuing its highly-regarded health sciences and nursing programs.

```html
<!DOCTYPE html>
<html lang="en">
<head>
<meta charset="utf-8">
<title>Alumni Ballot Postcard</title>
<link rel="stylesheet" href="https://fonts.googleapis.com/css2?family=Fira+Sans+Condensed:ital,wght@0,400;0,600;0,700;0,800;1,400;1,600;1,700;1,800;1,900&display=swap">
<style>
  :root {
    --navy: #1b4577;
    --ink: #173a66;
    --slate: #5f6f7c;
    --teal: #3dbfce;
    --teal-deep: #2aa7bd;
    --sky: #cde7f5;
    --sky-pale: #e4f2fa;
    --copper: #b8642a;
    --yellow: #ffe21a;
    --white: #ffffff;
    --page: #e9ecef;
    --rule: #5b6b7f;
  }
  * { box-sizing: border-box; margin: 0; padding: 0; }
  html, body { width: 1200px; height: 626px; overflow: hidden; }
  body {
    background: var(--page);
    font-family: "Fira Sans Condensed", "Arial Narrow", sans-serif;
    position: relative;
  }
  .postcard {
    position: absolute;
    top: 95px;
    width: 560px;
    height: 436px;
    overflow: hidden;
    background: var(--white);
    box-shadow: 0 2px 10px rgba(0,0,0,.18);
  }
  .postcard--front { left: 26px; }
  .postcard--back { left: 614px; }

  /* front */
  .photo { position: absolute; }
  .photo--keyboard {
    left: 0; top: 0; width: 378px; height: 210px;
    background: linear-gradient(135deg, #2b2f36 0%, #4b525c 40%, #2f6fb3 62%, #5aa6e4 78%, #3a3f47 100%);
  }
  .photo--key {
    left: 378px; top: 0; width: 182px; height: 246px;
    background: linear-gradient(160deg, #3a4048 0%, #2d78c4 35%, #4a9fe2 65%, #2f6eb0 100%);
  }
  .headline-band {
    position: absolute; left: 0; top: 210px; width: 378px; height: 36px;
    background: var(--slate);
    display: flex; align-items: center; padding-left: 18px;
  }
  .headline {
    color: var(--white); font-style: italic; font-weight: 800; font-size: 27px;
    letter-spacing: -.3px;
  }
  .headline__lead { font-size: 21px; }
  .message {
    position: absolute; left: 0; top: 246px; width: 378px; height: 190px;
    background:
      linear-gradient(90deg, transparent 0 62%, var(--sky-pale) 62% 100%),
      var(--sky);
    padding: 8px 14px 0 16px;
    color: var(--ink);
  }
  .message p {
    font-weight: 600; font-size: 12.4px; line-height: 1.36; text-align: justify;
    margin-bottom: 8px;
  }
  .dropcap {
    color: var(--copper); font-style: italic; font-weight: 800; font-size: 19px; line-height: 1;
  }
  .contact { display: flex; align-items: center; gap: 8px; margin-top: 4px; }
  .contact__icon { width: 27px; height: 27px; flex: none; }
  .contact__label { font-style: italic; font-size: 11.5px; color: var(--ink); line-height: 1.1; }
  .contact__email { font-style: italic; font-weight: 700; font-size: 13.5px; color: var(--copper); line-height: 1.1; }

  .side-strip {
    position: absolute; left: 378px; top: 246px; width: 182px; height: 24px;
    background: var(--teal);
  }
  .side-logo {
    position: absolute; left: 378px; top: 270px; width: 182px; height: 82px;
    background: var(--white);
  }
  .side-call {
    position: absolute; left: 378px; top: 352px; width: 182px; height: 84px;
    background: linear-gradient(180deg, var(--teal) 0%, var(--teal-deep) 100%);
    padding: 12px 6px 0 4px;
  }
  .call__small {
    font-style: italic; font-weight: 800; font-size: 12.5px; color: var(--white); letter-spacing: -.2px;
  }
  .call__big {
    font-style: italic; font-weight: 900; font-size: 32px; line-height: 1; color: var(--yellow);
    letter-spacing: -.8px; text-shadow: 0 2px 0 var(--ink);
  }

  .brand { position: absolute; display: flex; align-items: center; gap: 9px; }
  .brand__mark { width: 30px; height: 30px; border-radius: 50%; background: var(--navy); flex: none; }
  .brand__name {
    font-weight: 600; font-size: 17px; line-height: 1.05; color: var(--navy);
  }
  .side-logo .brand { left: 12px; top: 18px; }
  .side-logo .brand__name { font-size: 15.5px; }

  /* back */
  .back-curve { position: absolute; left: 0; top: 0; width: 560px; height: 436px; }
  .postcard--back .brand { left: 18px; top: 26px; }
  .postcard--back .contact { position: absolute; left: 18px; top: 78px; margin: 0; }
  .postcard--back .contact__email { color: var(--navy); }
  .stamp-box {
    position: absolute; right: 22px; top: 24px; width: 104px; height: 108px;
    border: 1.5px solid var(--rule);
  }
  .address-lines {
    position: absolute; left: 278px; top: 272px; width: 258px; list-style: none;
  }
  .address-lines li { height: 28px; border-bottom: 1.5px solid var(--rule); }
</style>
</head>
<body>

<section class="postcard postcard--front" aria-label="Postcard front">
  <div class="photo photo--keyboard" role="img" aria-label="Photo of a computer keyboard with a blue Vote key"></div>
  <div class="photo photo--key" role="img" aria-label="Close-up photo of the blue Vote key"></div>

  <div class="headline-band">
    <h1 class="headline"><span class="headline__lead">Alumni:</span> Please Vote!</h1>
  </div>

  <div class="message">
    <p><span class="dropcap">O</span>ver the past year and a half, the Alumni Association Executive Committee has been working on a major revision to the Alumni Association bylaws. The goal is a stronger and more inclusive Alumni Association.</p>
    <p>In order to confirm the new bylaws we need alumni approval. Go to sgfcollege-example.edu/alumni-feedback to give us your responses to the proposed bylaws and to vote on a new slate of officers.</p>
    <div class="contact">
      <svg class="contact__icon" viewBox="0 0 28 28" aria-hidden="true">
        <circle cx="14" cy="14" r="13" fill="#1b4577"/>
        <rect x="7" y="9" width="14" height="10" rx="1" fill="#fff"/>
        <path d="M7.5 9.5 14 15l6.5-5.5" fill="none" stroke="#1b4577" stroke-width="1.3"/>
      </svg>
      <div>
        <div class="contact__label">If you have questions, please E-mail us at:</div>
        <div class="contact__email">AlumniAssoc@sgfcollege-example.edu</div>
      </div>
    </div>
  </div>

  <div class="side-strip"></div>
  <div class="side-logo">
    <div class="brand">
      <span class="brand__mark" aria-hidden="true"></span>
      <span class="brand__name">Saint Gideon of<br>the Fields College</span>
    </div>
  </div>
  <div class="side-call">
    <div class="call__small">WE VALUE YOUR OPINION.</div>
    <div class="call__big">VOTE TODAY!</div>
  </div>
</section>

<section class="postcard postcard--back" aria-label="Postcard back">
  <svg class="back-curve" viewBox="0 0 560 436" aria-hidden="true">
    <path d="M0 150 C90 260 250 380 560 436 L0 436 Z" fill="#1b4577"/>
    <path d="M0 360 C120 400 240 420 330 436 L0 436 Z" fill="#a9c1dc"/>
    <path d="M0 150 C90 260 250 380 560 436" fill="none" stroke="#b8642a" stroke-width="1.5"/>
    <path d="M0 146 C92 258 252 376 560 430 L560 436 C250 380 90 260 0 150 Z" fill="#ffffff"/>
  </svg>

  <div class="brand">
    <span class="brand__mark" aria-hidden="true"></span>
    <span class="brand__name">Saint Gideon of<br>the Fields College</span>
  </div>
  <div class="contact">
    <svg class="contact__icon" viewBox="0 0 28 28" aria-hidden="true">
      <circle cx="14" cy="14" r="13" fill="#1b4577"/>
      <rect x="7" y="9" width="14" height="10" rx="1" fill="#fff"/>
      <path d="M7.5 9.5 14 15l6.5-5.5" fill="none" stroke="#1b4577" stroke-width="1.3"/>
    </svg>
    <div>
      <div class="contact__label">If you have questions, please E-mail us at:</div>
      <div class="contact__email">AlumniAssoc@sgfcollege-example.edu</div>
    </div>
  </div>

  <div class="stamp-box" aria-label="Stamp area"></div>
  <ul class="address-lines" aria-label="Address lines">
    <li></li><li></li><li></li><li></li>
  </ul>
</section>

</body>
</html>
```